Postcard for Direct Mailing

I need a Postcard Design that could be used for a direct mailing campaign. I just started a company called BrightLoom (www.brightloom-demo.net) which is an Administrating Consulting Services Company. It is basically a mix of being a Project Manager/Business Analysis/and Virtual Assistant.
My motto is "A Modern Solution to a Classic Problem"

The files that I attached I purchased from stock photos. and I would like them merged together for 1 side that shows how the problem with office staff has been forever.

Also the last one is my logo that should be on the side of the postcard where it can be sent out.

Below I have attached content. I'm not sure if it is too much.

Potential One Side
Are you losing time that could be better spent creating new business leads and focusing on the work at hand?
Worrying about the office work doesn't get it done …..
It may seem like modern technology would streamline your office processes to the point where you can do it all on your own without an assistance, but there is still only so much you can do to strike balance in the midst of running a thriving business.
That’s where BrightLoom Administrative Consulting Services steps in!

Potential Second Side
Let us take that load off your shoulders, while we assist with the taking over tasks that are cutting into your productivity. With the right assistance—or team—fighting on your behalf to create order, I act as another extension of your business and help you with your administrative support needs so that you can concentrate on what really matters – growing your business!
As a part of this customized service, we will take care of the following tasks:
• Word Processing
• Spreadsheet Creation/Tracking
• Research Services
• SlideCraft and other Presentations
• Database Management
• Data Entry
• Internet Research
• Client Relationship Management
• Email Management
• Calendar Management
• Conference Calls
• Vendor Management

Call today for further information, or to arrange a free consultation to determine which services we can provide for you call us at (800) 555-0147 or visit the site www.brightLOOM-demo.net TODAY!

```html
<!DOCTYPE html>
<html lang="en">
<head>
<meta charset="utf-8">
<title>BrightLoom Direct Mail Postcard</title>
<link rel="stylesheet" href="https://fonts.googleapis.com/css2?family=Fredoka:wght@500;600&family=Cabin:wght@400;600&display=swap">
<style>
  :root {
    --stage: #ebe8e3;
    --sky-blue: #1f9bf2;
    --violet: #9534cf;
    --lime: #6fe33a;
    --band-green: #33c832;
    --white: #ffffff;
    --paper: #f3f3f3;
    --ink: #2e2e2e;
    --charcoal: #2a2a2a;
    --faint-mark: #c4c4c4;
  }
  * { box-sizing: border-box; margin: 0; padding: 0; }
  html, body {
    width: 1200px; height: 497px; overflow: hidden;
    background: var(--stage);
  }
  .canvas { position: relative; width: 1200px; height: 497px; }

  /* Front side */
  .postcard-front {
    position: absolute; left: 26px; top: 28px;
    width: 562px; height: 400px; overflow: hidden;
    background: var(--sky-blue);
    font-family: "Fredoka", sans-serif;
    color: var(--white);
    box-shadow: 0 2px 6px rgba(0,0,0,.25);
  }
  .photo {
    position: absolute; top: 200px; height: 188px;
  }
  .photo-vintage-office {
    left: 0; width: 280px;
    background: linear-gradient(160deg, #8c8c8c 0%, #5a5a5a 45%, #3a3a3a 100%);
  }
  .photo-modern-office {
    left: 280px; width: 282px;
    background: linear-gradient(170deg, #f4f4f4 0%, #d9dde2 40%, #9aa4ae 100%);
  }
  .violet-panel { position: absolute; inset: 0; }
  .brand-mark {
    position: absolute; left: 22px; top: 80px;
    display: flex; align-items: center; gap: 7px;
    font-weight: 600; font-size: 27px; color: var(--lime);
  }
  .brand-mark .dot {
    width: 16px; height: 16px; border-radius: 50%; background: var(--lime);
  }
  .headline {
    position: absolute; left: 210px; width: 340px; top: 22px;
    text-align: center; font-weight: 600; font-size: 16.5px;
    color: var(--lime);
  }
  .pitch {
    position: absolute; left: 212px; width: 326px;
    font-weight: 600; font-size: 8.8px; line-height: 12px;
    text-align: center;
  }
  .pitch-question { top: 56px; }
  .pitch-worry { top: 92px; }
  .pitch-reality { top: 113px; text-align: justify; text-align-last: left; }
  .pitch-answer { top: 175px; }
  .web-band {
    position: absolute; left: 0; bottom: 0; width: 100%; height: 14px;
    background: var(--band-green);
  }
  .web-address {
    position: absolute; left: 0; width: 280px; bottom: 1px;
    text-align: center; font-weight: 600; font-size: 11px; letter-spacing: .3px;
  }

  /* Back side */
  .postcard-back {
    position: absolute; left: 614px; top: 67px;
    width: 560px; height: 400px; overflow: hidden;
    background: var(--paper);
    font-family: "Cabin", sans-serif; color: var(--ink);
    box-shadow: 0 2px 6px rgba(0,0,0,.25);
  }
  .intro {
    position: absolute; left: 24px; right: 24px; top: 20px;
    font-size: 11px; line-height: 14.2px; text-align: justify;
  }
  .task-lead {
    position: absolute; left: 24px; top: 98px; font-size: 11px;
  }
  .task-list {
    position: absolute; left: 24px; top: 130px; list-style: none;
    font-size: 11px; line-height: 15.5px;
  }
  .task-list li { padding-left: 19px; position: relative; }
  .task-list li::before {
    content: "·"; position: absolute; left: 0; top: 0;
  }
  .faint-brand {
    position: absolute; left: 350px; top: 200px;
    display: flex; align-items: center; gap: 8px;
    font-family: "Cabin", sans-serif; font-weight: 600; font-size: 28px;
    color: var(--faint-mark);
  }
  .faint-brand .dot {
    width: 18px; height: 18px; border-radius: 50%; background: var(--faint-mark);
  }
  .divider { position: absolute; left: 0; top: 328px; width: 560px; height: 12px; }
  .call-band {
    position: absolute; left: 0; bottom: 0; width: 100%; height: 63px;
    background: var(--charcoal); color: var(--white);
    font-size: 11px; line-height: 14.5px; text-align: center;
    padding: 13px 14px 0;
  }
  .call-band strong { font-weight: 600; }
</style>
</head>
<body>
<main class="canvas">

  <section class="postcard-front">
    <div class="photo photo-vintage-office" role="img" aria-label="Black and white photo of a busy 1920s office with clerks and typists"></div>
    <div class="photo photo-modern-office" role="img" aria-label="Photo of stressed modern office workers in shirts and ties at a desk"></div>

    <svg class="violet-panel" width="562" height="400" viewBox="0 0 562 400" aria-hidden="true">
      <path d="M206 0 H562 V236 C470 222 330 206 232 224 C208 170 196 90 206 0 Z" fill="var(--violet)"/>
    </svg>

    <div class="brand-mark"><span class="dot"></span>BrightLoom</div>

    <h1 class="headline">A Modern Solution to a Classic Problem</h1>
    <p class="pitch pitch-question">Are you losing time that could be better spent<br>creating new business leads and focusing on the work at hand?</p>
    <p class="pitch pitch-worry">Worrying about the office work doesn't get it done …..</p>
    <p class="pitch pitch-reality">It may seem like modern technology would streamline your office processes to the point where you can do it all on your own without an assistance, but there is still only so much you can do to strike balance in the midst of running a thriving business.</p>
    <p class="pitch pitch-answer">That's where BrightLoom Administrative Consulting Services steps in!</p>

    <div class="web-band"></div>
    <p class="web-address">www.brightLOOM-demo.net</p>
  </section>

  <section class="postcard-back">
    <p class="intro">Let us take that load off your shoulders, while we assist with the taking over tasks that are cutting into your productivity. With the right assistance—or team—fighting on your behalf to create order, I act as another extension of your business and help you with your administrative support needs so that you can concentrate on what really matters – growing your business!</p>
    <p class="task-lead">As a part of this customized service, we will take care of the following tasks:</p>
    <ul class="task-list">
      <li>Word Processing</li>
      <li>Spreadsheet Creation/Tracking</li>
      <li>Research Services</li>
      <li>SlideCraft and other Presentations</li>
      <li>Database Management</li>
      <li>Data Entry</li>
      <li>Internet Research</li>
      <li>Client Relationship Management</li>
      <li>Email Management</li>
      <li>Calendar Management</li>
      <li>Conference Calls</li>
      <li>Vendor Management</li>
    </ul>

    <div class="faint-brand"><span class="dot"></span>BrightLoom</div>

    <svg class="divider" width="560" height="12" viewBox="0 0 560 12" aria-hidden="true">
      <path d="M0 10 Q280 -2 560 8" fill="none" stroke="var(--charcoal)" stroke-width="1.5"/>
    </svg>
    <div class="call-band">
      Call today for further information, or to arrange a free consultation to determine which services<br>
      we can provide for you call us at <strong>(800) 555-0147</strong> or visit the site <strong>www.brightLOOM-demo.net</strong> TODAY!
    </div>
  </section>

</main>
</body>
</html>
```